Cellar Crew Poster / Flyer Ad Design

We need a poster design (and a complimentary A6 flyer) to promote our Adult Rock Band Course called 'Cellar Crew'.

Target market is adults aged 25 - 50 primarily

Design to be eye catching, creative, appealing and easy to understand. Most of the distribution will be street marketing, email marketing, social media, music magazines and websites and to other music teachers.

We need the design to be as an A3 and A4 poster and an A6 promo flyer/e-flyer. Should look good in colour and we'll want a version in black and white.

Would be good to also incorporate our music school logo (just for branding purposes).

Text as follows:

CELLAR CREW
The Ultimate Rock Band Course for Adults

Ever wondered what it would be like to play in a band?

Feeling musically rusty and looking for a way to start playing your instrument again?

Then here’s an exciting opportunity you can’t miss!

All musical levels
Beginner/Intermediate to Advanced Players

Limited Numbers

REGISTER ONLINE NOW
www.tunewellstudio.com.au

Starts Saturday 3rd August
Newtown

Over 6 exciting weekends you’ll work with one of our experienced professional band coaches and transform yourselves into the ultimate ‘Cellar Crew’

Discover how to play in a band
Revisit your musical abilities
Practice songs
Perform on Stage

Drummers, Bass Guitarists, Singers, Keys, Guitarists, Saxophone, Percussionists and others all welcome to join

For more information, course costs and registration, please visit www.tunewellstudio.com.au or call 02 7391 4825 / 0438 572 904

Reason: Hi Everyone, I've been away and unable to respond to some of the designs because I've been ill. Have decided to extend the deadline and now commit to paying designers. Look forward to seeing more designs. Any questions, please let me know. Thanks Melinda

```html
<!DOCTYPE html>
<html lang="en">
<head>
<meta charset="utf-8">
<title>Cellar Crew – Rock Band Course Poster</title>
<link rel="stylesheet" href="https://fonts.googleapis.com/css2?family=Black+Ops+One&family=Oswald:wght@500;700&family=Roboto+Condensed:wght@700&family=Montserrat:wght@600;700&display=swap">
<style>
  :root {
    --ink: #111111;
    --wall-dark: #1f1f1f;
    --wall-mid: #4a4a4a;
    --wall-light: #6b6b6b;
    --white: #ffffff;
    --paper: #f2f2f2;
    --grey-light: #c9c9c9;
    --grey-mid: #9a9a9a;
    --grey-box: #a8a8a8;
    --photo-dark: #2b2b2b;
    --photo-mid: #5c5c5c;
  }
  html, body {
    margin: 0;
    padding: 0;
    overflow: hidden;
    background: var(--wall-dark);
  }
  .poster {
    position: relative;
    width: 853px;
    height: 1200px;
    overflow: hidden;
    background: radial-gradient(ellipse at 55% 38%, var(--wall-light) 0%, var(--wall-mid) 40%, var(--wall-dark) 100%);
    color: var(--white);
  }
  .brand {
    position: absolute;
    left: 96px;
    top: 52px;
    width: 560px;
    text-align: center;
  }
  .brand-name {
    font-family: "Montserrat", sans-serif;
    font-weight: 600;
    font-size: 52px;
    line-height: 1;
    letter-spacing: -1px;
    color: var(--grey-light);
  }
  .brand-tagline {
    margin-top: 10px;
    font-family: "Montserrat", sans-serif;
    font-weight: 700;
    font-size: 17px;
    letter-spacing: 0.5px;
    color: var(--paper);
  }
  .brand-dot {
    position: absolute;
    left: 628px;
    top: 38px;
    width: 116px;
    height: 116px;
    border-radius: 50%;
    background: var(--grey-mid);
  }
  .course-title {
    position: absolute;
    left: 20px;
    top: 150px;
    width: 810px;
    margin: 0;
    text-align: center;
    font-family: "Black Ops One", sans-serif;
    font-weight: 400;
    font-size: 118px;
    line-height: 0.92;
    color: var(--paper);
    transform: rotate(-5deg);
    text-shadow: 4px 5px 0 #7d7d7d, 8px 10px 10px rgba(0,0,0,0.5);
  }
  .course-title span { display: block; }
  .course-title .first { padding-right: 120px; }
  .course-title .second { padding-left: 300px; }
  .band-photo {
    position: absolute;
    left: 160px;
    top: 362px;
    width: 544px;
    height: 300px;
    background: linear-gradient(180deg, var(--photo-mid) 0%, var(--photo-dark) 70%, rgba(43,43,43,0) 100%);
  }
  .headline {
    position: absolute;
    left: 0;
    top: 606px;
    width: 853px;
    margin: 0;
    text-align: center;
    font-family: "Oswald", sans-serif;
    font-weight: 700;
    font-size: 72px;
    line-height: 1.0;
    color: var(--white);
    text-shadow: 0 3px 8px rgba(0,0,0,0.6);
  }
  .subhead-bar {
    position: absolute;
    left: 55px;
    top: 784px;
    width: 741px;
    height: 54px;
    background: var(--ink);
    border: 2px solid var(--white);
    outline: 3px solid var(--ink);
    display: flex;
    align-items: center;
    justify-content: center;
    font-family: "Oswald", sans-serif;
    font-weight: 700;
    font-size: 37px;
    color: var(--white);
  }
  .details {
    font-family: "Roboto Condensed", sans-serif;
    font-weight: 700;
    font-size: 16px;
    line-height: 1.13;
    text-transform: uppercase;
    color: var(--white);
  }
  .details p { margin: 0 0 13px; }
  .details-left {
    position: absolute;
    right: 514px;
    top: 870px;
    width: 320px;
    text-align: right;
  }
  .details-right {
    position: absolute;
    left: 517px;
    top: 870px;
    width: 320px;
    text-align: left;
  }
  .start-box {
    position: absolute;
    left: 381px;
    top: 862px;
    width: 118px;
    height: 206px;
    box-sizing: border-box;
    padding-top: 7px;
    background: var(--grey-box);
    color: var(--ink);
    text-align: center;
  }
  .start-box .when {
    font-family: "Oswald", sans-serif;
    font-weight: 700;
    font-size: 21px;
    line-height: 1.08;
  }
  .start-box .early {
    margin-top: 7px;
    font-family: "Roboto Condensed", sans-serif;
    font-weight: 700;
    font-size: 12px;
    line-height: 1.15;
    color: var(--white);
  }
  .start-box .limited {
    margin-top: 7px;
    font-family: "Roboto Condensed", sans-serif;
    font-weight: 700;
    font-size: 12px;
  }
  .register {
    position: absolute;
    left: 0;
    top: 1094px;
    width: 853px;
    text-align: center;
    font-family: "Oswald", sans-serif;
    font-weight: 700;
    font-size: 31px;
    color: var(--white);
  }
  .register .web { color: var(--grey-light); }
  .contact {
    position: absolute;
    left: 0;
    top: 1146px;
    width: 853px;
    text-align: center;
    font-family: "Roboto Condensed", sans-serif;
    font-weight: 700;
    font-size: 16px;
    color: var(--white);
  }
</style>
</head>
<body>
<main class="poster">
  <header>
    <div class="brand">
      <div class="brand-name">tunewellstudio</div>
      <div class="brand-tagline">YOU’RE NEVER TOO YOUNG OR TOO OLD</div>
    </div>
    <div class="brand-dot" aria-hidden="true"></div>
  </header>

  <h1 class="course-title"><span class="first">CELLAR</span><span class="second">CREW</span></h1>

  <div class="band-photo" role="img" aria-label="Photo of three musicians in sunglasses: a bass player, a singer with a microphone and a guitarist, posed against a brick wall"></div>

  <h2 class="headline">ALWAYS WANTED<br>TO PLAY IN A BAND?</h2>

  <div class="subhead-bar">THE ULTIMATE ROCK BAND COURSE FOR ADULTS</div>

  <section class="details details-left">
    <p>Feeling musically rusty?<br>Then here's an opportunity<br>you can't miss!</p>
    <p>All musical levels<br>Beginner/Intermediate to Advanced</p>
    <p>Drummers, bass guitarists, singers,<br>keys, guitarists, saxophone,<br>percussionists and others<br>all welcome to join</p>
  </section>

  <div class="start-box">
    <div class="when">STARTS<br>SATURDAY<br>3RD AUGUST<br>NEWTOWN</div>
    <div class="early">REGISTER EARLY<br>FOR EARLY<br>BIRD DISCOUNT</div>
    <div class="limited">LIMITED NUMBERS</div>
  </div>

  <section class="details details-right">
    <p>Discover how to play in a band.<br>Revisit your musical abilities.<br>Practice songs. Perform on stage.</p>
    <p>Over 6 exciting weekends<br>you'll work with one of our<br>experienced professional<br>band coaches and transform<br>yourselves into the ultimate<br>'Cellar Crew'</p>
  </section>

  <footer>
    <div class="register">REGISTER ONLINE NOW <span class="web">WWW.TUNEWELLSTUDIO.COM.AU</span></div>
    <div class="contact">FOR MORE INFORMATION, COURSE COSTS AND REGISTRATION CALL 02 7391 4825 / 0438 572 904</div>
  </footer>
</main>
</body>
</html>
```